card design for engineering consultancy

engineering drafting and project management company the provides drafting services for.
Electrical, Hydraulic, Mechanical, and Civil services
The company is called Q7R Services and logo is as attached
Information on card should be.
1. Logo
2.website : Q7RServices.example
3. email : info@Q7RServices.example
4. Phone: (+61) 400512836
5. Motto: Design - Document - Develop - Deliver

this card should be basically used for business identification only

Target Market(s)

electricians plumbers air conditioning installers and civil contractors

Industry/Entity Type

engineering, drafting, electrical, plumbing, airconditioning, civil

Contact Information for Business Card

1. Logo 2.website : Q7RServices.example 3. email : info@Q7RServices.example 4. Phone: (+61) 400512836 5. Motto: Design - Document - Develop - Deliver

Font styles to use
Serif

Requirements
Must have
• logo
Nice to have
• something inovative and different that makes it stand out from being just another business card

```html
<!DOCTYPE html>
<html lang="en">
<head>
<meta charset="utf-8">
<title>Q7R Services – Business Card</title>
<link rel="stylesheet" href="https://fonts.googleapis.com/css2?family=Michroma&family=Open+Sans:wght@400;600&display=swap">
<style>
  :root {
    --backdrop: #d9d9d9;
    --card-white: #ffffff;
    --card-dark: #3b3b3d;
    --ink-dark: #3a3a3c;
    --ink-muted: #555558;
    --brand-red: #c8101e;
    --ink-light: #f2f2f2;
  }
  * { margin: 0; padding: 0; box-sizing: border-box; }
  html, body {
    width: 1200px; height: 800px; overflow: hidden;
    background: var(--backdrop);
  }
  .stage {
    width: 1200px; height: 800px;
    display: flex; align-items: center; justify-content: center; gap: 40px;
  }
  .card {
    position: relative;
    width: 540px; height: 310px;
    border-radius: 22px;
    overflow: hidden;
  }
  .card--front { background: var(--card-white); }
  .card--back { background: var(--card-dark); }

  /* Front card */
  .brand-mark {
    position: absolute; top: 34px; right: 34px;
    display: flex; align-items: center; gap: 12px;
    font-family: "Michroma", sans-serif;
    font-size: 22px; color: var(--ink-dark);
    letter-spacing: 1px;
  }
  .brand-mark__square {
    width: 18px; height: 18px; background: var(--brand-red);
  }
  .contact-block {
    position: absolute; left: 40px; bottom: 38px;
  }
  .person-name {
    font-family: "Michroma", sans-serif;
    font-size: 19px; color: var(--ink-dark);
    letter-spacing: 1px; text-transform: uppercase;
  }
  .person-role {
    font-family: "Open Sans", sans-serif;
    font-size: 15px; color: var(--brand-red);
    margin-top: 2px; margin-bottom: 14px;
  }
  .contact-list { list-style: none; }
  .contact-list li {
    display: flex; align-items: center; gap: 10px;
    font-family: "Open Sans", sans-serif;
    font-size: 14px; color: var(--ink-muted);
    line-height: 22px;
  }
  .contact-icon { width: 12px; height: 12px; flex: none; }

  /* Back card */
  .back-brand {
    position: absolute; left: 0; right: 0; top: 108px;
    text-align: center;
    font-family: "Michroma", sans-serif;
    font-size: 34px; color: var(--ink-light);
    letter-spacing: 3px;
  }
  .motto {
    position: absolute; left: 0; right: 0; bottom: 44px;
    display: flex; justify-content: center; align-items: center; gap: 8px;
    font-family: "Open Sans", sans-serif;
    font-size: 13px; color: var(--ink-light);
    letter-spacing: 0.5px; text-transform: uppercase;
  }
  .motto__tick { width: 12px; height: 12px; flex: none; }
</style>
</head>
<body>
<main class="stage">
  <section class="card card--front">
    <div class="brand-mark">
      <span class="brand-mark__square"></span>
      <span class="brand-mark__name">Q7R Services</span>
    </div>
    <div class="contact-block">
      <p class="person-name">Daniel Hart</p>
      <p class="person-role">President</p>
      <ul class="contact-list">
        <li>
          <svg class="contact-icon" viewBox="0 0 12 12" aria-hidden="true"><path d="M2.5 1 L4.5 1 L5 3.5 L3.8 4.4 Q5 7 7.6 8.2 L8.5 7 L11 7.5 L11 9.5 Q10.5 11 9 11 Q1 10 1 3 Q1 1.5 2.5 1 Z" fill="var(--brand-red)"/></svg>
          <span>(+61) 400512836</span>
        </li>
        <li>
          <svg class="contact-icon" viewBox="0 0 12 12" aria-hidden="true"><rect x="0.5" y="2.5" width="11" height="7.5" fill="var(--brand-red)"/><path d="M0.5 2.5 L6 7 L11.5 2.5" fill="none" stroke="#fff" stroke-width="1"/></svg>
          <span>info@Q7RServices.example</span>
        </li>
        <li>
          <svg class="contact-icon" viewBox="0 0 12 12" aria-hidden="true"><circle cx="6" cy="6" r="5.5" fill="var(--brand-red)"/><path d="M0.5 6 H11.5 M6 0.5 Q3 6 6 11.5 M6 0.5 Q9 6 6 11.5" fill="none" stroke="#fff" stroke-width="0.8"/></svg>
          <span>Q7RServices.example</span>
        </li>
      </ul>
    </div>
  </section>

  <section class="card card--back">
    <p class="back-brand">Q7R Services</p>
    <p class="motto">
      <span>Design</span>
      <svg class="motto__tick" viewBox="0 0 12 12" aria-hidden="true"><circle cx="6" cy="6" r="5" fill="none" stroke="var(--brand-red)" stroke-width="1.4"/><path d="M3.5 6 L5.5 8 L9 4" fill="none" stroke="var(--brand-red)" stroke-width="1.4"/></svg>
      <span>Document</span>
      <svg class="motto__tick" viewBox="0 0 12 12" aria-hidden="true"><circle cx="6" cy="6" r="5" fill="none" stroke="var(--brand-red)" stroke-width="1.4"/><path d="M3.5 6 L5.5 8 L9 4" fill="none" stroke="var(--brand-red)" stroke-width="1.4"/></svg>
      <span>Develop</span>
      <svg class="motto__tick" viewBox="0 0 12 12" aria-hidden="true"><circle cx="6" cy="6" r="5" fill="none" stroke="var(--brand-red)" stroke-width="1.4"/><path d="M3.5 6 L5.5 8 L9 4" fill="none" stroke="var(--brand-red)" stroke-width="1.4"/></svg>
      <span>Deliver</span>
    </p>
  </section>
</main>
</body>
</html>
```